Küchenparty
Zielgruppe
Restaurant / Catering / Event Management
Zielgruppe ü 40
Aufgabenstellung
Klares, schlichtes und vorallem edles design
Den Valentinstag mal anders feiern?
mischen Sie sich mit Ihren Liebsten ins getrubel einer Großküche und erleben das exclusive Küchenflair!
Bunte Diskobeläuchtung, Musik und Gäste in der Küche....das gibt es nur zu ganz besonderen Anlässen!
Endlich haben Sie in unserer komplett neu renovierten Küche wieder die Möglichkeit unseren Köchen und Köchinnen über die Schulter zu schauen oder über Rezepte fachzusimpeln.
Wir freuen uns Sie zur ersten Küchenparty im Lindmarks am See begrüßen zu dürfen!
Es erwartet Sie eine Veilzahl an speziell für Sie angerichteten Speisen.
Dazu genießen Sie Weine regionaler Weingüter und aus Italien.
Speisen und Getränke inclusive!
Preis pro Person 98€
Den Valentinstag mal anders beginnen;
mit höchstem Genuss aus Küche und Keller bei der Küchenparty im Lindmks am See.
Schlagsworte:
Für Sie individuell angerichtete Speisen / die Küche in action für Sie!
Weine der Region
DJ und Party
Preis 98,00 €
inklusive:
Aperitif
Große Speisenvarietät (5 Gänge plus)
Regionale und italienische Weine
Logo muss vorhanden sein in rot odeer weiss
Kontaktdaten:
Lindmarks am See
Lore-Falk platz 7
71058 Böblingen
Tel: 07031 38 716 0
Mail: event@lindmarks.de
www.lindmarks.de

```html
<!DOCTYPE html>
<html lang="de">
<head>
<meta charset="utf-8">
<title>Küchenparty – Lindmarks am See</title>
<link rel="stylesheet" href="https://fonts.googleapis.com/css2?family=Poiret+One&display=swap">
<style>
  :root {
    --gold: #d4b04f;
    --gold-text: #d9b75c;
    --ink: #1f1f22;
    --copy: #2c2c30;
    --contact: #3a3a3e;
    --logo-red: #a8312c;
    --white: #ffffff;
  }
  * { box-sizing: border-box; margin: 0; padding: 0; }
  html, body { width: 1200px; height: 1200px; overflow: hidden; background: var(--white); }
  body { position: relative; font-family: "Poiret One", sans-serif; }

  .card {
    position: absolute; left: 10px; width: 1160px; overflow: hidden;
    box-shadow: 3px 4px 6px rgba(0,0,0,.35);
  }
  .card--front { top: 5px; height: 546px; }
  .card--back { top: 579px; height: 547px; }

  .glitter-photo {
    position: absolute; inset: 0;
    background:
      radial-gradient(ellipse 70% 18% at 45% 72%, rgba(190,150,80,.75), rgba(190,150,80,0) 70%),
      linear-gradient(180deg, #1d3d4c 0%, #2b5560 30%, #1c3a4a 55%, #3a3a30 75%, #15232e 100%);
  }

  .title {
    position: absolute; left: 162px; top: 112px;
    font-size: 146px; line-height: 1; color: var(--gold-text);
    letter-spacing: -2px; font-weight: 400; white-space: nowrap;
  }

  .brand { position: absolute; font-family: "Poiret One", sans-serif; font-weight: 400; white-space: nowrap; }
  .brand--front { right: 52px; bottom: 44px; font-size: 36px; color: var(--white); }
  .brand--back {
    left: 288px; top: 400px; width: 160px;
    font-size: 25px; line-height: 26px; color: var(--logo-red); text-align: right;
  }

  .panel {
    position: absolute; left: 56px; top: 56px; width: 1050px; height: 435px;
    border: 7px solid var(--gold); background: rgba(228,233,238,.94);
  }
  .headline {
    position: absolute; left: 145px; top: 84px;
    font-size: 44px; font-weight: 400; color: var(--ink); white-space: nowrap;
  }
  .copy { position: absolute; left: 288px; font-size: 23px; line-height: 27px; color: var(--copy); white-space: nowrap; }
  .copy--intro { top: 178px; }
  .copy--menu { top: 258px; }
  .copy--wine { top: 341px; }

  .contact { position: absolute; top: 414px; font-size: 16px; line-height: 19px; color: var(--contact); white-space: nowrap; }
  .contact--address { left: 468px; }
  .contact--reach { left: 614px; }

  .photo-circle { position: absolute; border-radius: 50%; border: 3px solid var(--gold); }
  .photo-circle--dinner {
    left: -30px; top: 138px; width: 240px; height: 240px;
    background: radial-gradient(circle at 60% 40%, #5a3030, #3b2a28 55%, #c9a98a 100%);
  }
  .photo-circle--champagne {
    left: 0; top: 374px; width: 188px; height: 188px;
    background: radial-gradient(circle at 50% 40%, #b59a60, #4a3a22 55%, #1a1510 100%);
  }
  .photo-circle--chocolate {
    left: 950px; top: 3px; width: 212px; height: 212px;
    background: radial-gradient(circle at 50% 55%, #9b5a34, #5a2e1a 60%, #3a1c10 100%);
  }

  .price-badge {
    position: absolute; left: 824px; top: 267px; width: 264px; height: 264px;
    border-radius: 50%; background: var(--white); border: 5px solid var(--gold);
    display: flex; align-items: center; justify-content: center; text-align: center;
    color: var(--gold-text); font-size: 22px; line-height: 25px;
  }
</style>
</head>
<body>

<section class="card card--front">
  <div class="glitter-photo" role="img" aria-label="Dunkelblauer Bokeh-Hintergrund mit goldenem Glitzer"></div>
  <h1 class="title">Küchenparty</h1>
  <div class="brand brand--front">Lindmarks am See</div>
</section>

<section class="card card--back">
  <div class="glitter-photo" role="img" aria-label="Dunkelblauer Bokeh-Hintergrund mit goldenem Glitzer"></div>
  <div class="panel"></div>

  <h2 class="headline">Den Valentinstag mal anders beginnen</h2>
  <p class="copy copy--intro">mit höchstem Genuss aus Küche und Keller<br>bei der Küchenparty im Lindmks am See.</p>
  <p class="copy copy--menu">Für Sie individuell angerichtete Speise<br>die Küche in action für Sie!</p>
  <p class="copy copy--wine">Weine der Region – DJ und Party</p>

  <div class="brand brand--back">Lindmarks<br>am See</div>
  <p class="contact contact--address">Lindmarks am See<br>Lore-Falk platz 7<br>71058 Böblingen</p>
  <p class="contact contact--reach">Tel: 07031 38 716 0<br>Mail: event@lindmarks.de<br>www.lindmarks.de</p>

  <div class="photo-circle photo-circle--dinner" role="img" aria-label="Festlich angerichteter Teller mit Rotweinglas im Restaurant"></div>
  <div class="photo-circle photo-circle--champagne" role="img" aria-label="Zwei anstoßende Sektgläser"></div>
  <div class="photo-circle photo-circle--chocolate" role="img" aria-label="Schokolade und Pralinen"></div>

  <div class="price-badge">
    <p>Preis 98,00 €<br>inklusive: Aperitif<br>Grosse Speisenvarietät<br>(5 Gänge plus)<br>Regionale und<br>italienische Weine</p>
  </div>
</section>

</body>
</html>
```